Vegan bakery needs business card

We need a business card design for my vegan bakery in Philadelphia Pa. We create amazing whole food plant based cuisine that is egg and dairy free. We use fruits, vegetables, healing herbs, nuts, natural sugars (date, turbinado, agave) and non bleached flours in our creations. Due to demand and interest in the Philadelphia area we created a late night vegan dessert delivery service named Moonlark Greens. We are the only business providing delicious vegan desserts delivered to your door at 1am!! We would like to see designs that use the color scheme in the logo. The final design should communicate the benefits of our products: dairy/egg free, plant based, healing herbs, amazing food.

Industry/Entity Type

Business

```html
<!DOCTYPE html>
<html lang="en">
<head>
<meta charset="utf-8">
<title>Moonlark Greens – Business Card</title>
<link href="https://fonts.googleapis.com/css2?family=Arimo:wght@400&family=Nunito:wght@700;800&display=swap" rel="stylesheet">
<style>
  :root {
    --coral: #ef7a63;
    --ink: #3d3d3d;
    --paper: #ffffff;
    --backdrop: #e9e9e9;
  }
  * { margin: 0; padding: 0; box-sizing: border-box; }
  html, body { width: 1200px; height: 675px; overflow: hidden; }
  body {
    background: var(--backdrop);
    display: flex;
    align-items: center;
    justify-content: center;
    gap: 50px;
  }
  .card {
    position: relative;
    width: 540px;
    height: 309px;
    background: var(--paper);
    box-shadow: 0 6px 18px rgba(0,0,0,0.12);
    overflow: hidden;
  }

  /* Brand name */
  .brand {
    position: absolute;
    display: flex;
    align-items: center;
    gap: 8px;
    font-family: "Nunito", sans-serif;
    font-weight: 800;
    color: var(--coral);
    white-space: nowrap;
  }
  .brand-dot {
    border-radius: 50%;
    background: var(--coral);
    flex: none;
  }

  /* Front */
  .card-front .brand {
    left: 0; right: 0;
    top: 108px;
    justify-content: center;
    font-size: 38px;
  }
  .card-front .brand-dot { width: 22px; height: 22px; }
  .benefit-band {
    position: absolute;
    left: 0; right: 0;
    top: 214px;
    height: 30px;
    background: var(--coral);
    color: var(--paper);
    font-family: "Nunito", sans-serif;
    font-weight: 700;
    font-size: 16px;
    letter-spacing: 0.2px;
    display: flex;
    align-items: center;
    justify-content: center;
  }

  /* Back */
  .card-back .brand {
    right: 26px;
    top: 96px;
    font-size: 27px;
  }
  .card-back .brand-dot { width: 16px; height: 16px; }

  .contact {
    position: absolute;
    left: 0; top: 52px;
    font-family: "Arimo", sans-serif;
    color: var(--ink);
  }
  .person {
    display: flex;
    align-items: stretch;
    gap: 18px;
    font-size: 14px;
    line-height: 1.2;
  }
  .person-marker {
    width: 30px;
    height: 38px;
    background: var(--coral);
    margin-top: 8px;
  }
  .address {
    margin: 38px 0 0 48px;
    font-size: 15px;
    line-height: 1.12;
  }
  .channels {
    list-style: none;
    margin: 20px 0 0 48px;
    font-size: 15px;
    line-height: 1.15;
  }
  .channels li { display: flex; align-items: center; gap: 8px; margin-bottom: 2px; }
  .channels svg { width: 14px; height: 14px; flex: none; }
</style>
</head>
<body>

  <section class="card card-front" aria-label="Business card front">
    <div class="brand"><span class="brand-dot"></span>Moonlark Greens</div>
    <div class="benefit-band">Dairy/egg free, Plant based, Healing Herbs, Amazing Food</div>
  </section>

  <section class="card card-back" aria-label="Business card back">
    <div class="contact">
      <div class="person">
        <span class="person-marker"></span>
        <p>Employee Name<br>Title</p>
      </div>
      <p class="address">Philly HQ<br>1480 Larkspur Avenue- Suite 210<br>Philadelphia, PA 19107</p>
      <ul class="channels">
        <li>
          <svg viewBox="0 0 14 14" aria-hidden="true"><rect width="14" height="14" rx="2" fill="var(--coral)"/><path d="M4 3.2c.6-.4 1.1-.3 1.4.2l.7 1.3c.2.4.1.8-.2 1.1l-.5.4c.4.9 1.2 1.7 2.1 2.1l.4-.5c.3-.3.7-.4 1.1-.2l1.3.7c.5.3.6.8.2 1.4-.6.9-1.6 1.2-2.6.7C6 9.6 4.4 8 3.6 6.1c-.5-1-.3-2.1.4-2.9z" fill="#fff"/></svg>
          (215) 555- 0147
        </li>
        <li>
          <svg viewBox="0 0 14 14" aria-hidden="true"><rect y="2" width="14" height="10" rx="1" fill="var(--coral)"/><path d="M1 3l6 5 6-5" fill="none" stroke="#fff" stroke-width="1.3"/></svg>
          Info@website.com
        </li>
        <li>
          <svg viewBox="0 0 14 14" aria-hidden="true"><g fill="none" stroke="var(--coral)" stroke-width="1.2"><circle cx="7" cy="7" r="6"/><ellipse cx="7" cy="7" rx="2.6" ry="6"/><path d="M1 7h12M2 4h10M2 10h10"/></g></svg>
          www.website.com
        </li>
      </ul>
    </div>
    <div class="brand"><span class="brand-dot"></span>Moonlark Greens</div>
  </section>

</body>
</html>
```